Visitenkarten-Design für Versicherungsmakler
Zielgruppe
Wir sind ein Versicherungsmakler aus Leipzig.
Aufgabenstellung
Im Anhang finden Sie die alte Visitenkarte. Die Daten können übernommen werden. Aber statt Inhaber bitte 'Geschäftsführer'
Die Farben sollten beibehalten werden. Bei der Frage ob das rot oder das grau die Primärfarbe ist, bin ich flexibel. Von der Gestaltung her sind Ihnen ansonsten keine Grenzen gesetzt.

```html
<!DOCTYPE html>
<html lang="de">
<head>
<meta charset="utf-8">
<title>Velario Finance Consulting – Visitenkarte</title>
<link href="https://fonts.googleapis.com/css2?family=Questrial&family=Montserrat:wght@600;800&family=Roboto+Condensed:wght@700&display=swap" rel="stylesheet">
<style>
  :root {
    --red-deep: #8f0009;
    --red: #d4131c;
    --red-bright: #ef1c26;
    --grey: #4a4a4f;
    --white: #ffffff;
    --stage: #e6e6e8;
  }
  * { margin: 0; padding: 0; box-sizing: border-box; }
  html, body { width: 1200px; height: 912px; overflow: hidden; }
  body {
    background: var(--stage);
    display: flex; flex-direction: column; align-items: center; justify-content: center;
    gap: 32px;
  }
  .card {
    width: 640px; height: 400px; position: relative; overflow: hidden;
    box-shadow: 0 6px 18px rgba(0,0,0,.18);
  }
  .card--front {
    background: linear-gradient(135deg, var(--red-deep) 0%, var(--red) 55%, var(--red-bright) 100%);
    color: var(--white);
  }
  .brand { position: absolute; font-family: "Questrial", sans-serif; }
  .brand__name { display: block; font-size: 96px; line-height: 1; letter-spacing: 2px; }
  .brand__tag { display: block; font-size: 22px; letter-spacing: 4px; margin-top: 8px; padding-left: 60px; }
  .card--front .brand { left: 150px; top: 95px; }
  .legal {
    position: absolute; left: 40px; right: 40px; bottom: 36px;
    font-family: "Roboto Condensed", sans-serif; font-weight: 700;
    font-size: 12.5px; line-height: 1.45; text-align: center; letter-spacing: .2px;
  }
  .card--back { background: var(--white); }
  .card--back .brand { left: 50px; top: 150px; }
  .card--back .brand__name { color: var(--red-bright); font-size: 64px; }
  .card--back .brand__tag { color: var(--grey); font-size: 15px; letter-spacing: 3px; padding-left: 30px; }
  .contact { position: absolute; left: 360px; top: 60px; }
  .contact__name {
    font-family: "Montserrat", sans-serif; font-weight: 800; color: var(--red-bright);
    font-size: 28px; letter-spacing: .5px;
  }
  .contact__role {
    font-family: "Questrial", sans-serif; color: var(--grey); font-size: 14px;
    letter-spacing: 4px; margin: 2px 0 22px;
  }
  .contact__list { list-style: none; }
  .contact__list li {
    display: flex; align-items: center; gap: 10px;
    font-family: "Montserrat", sans-serif; font-size: 14px; color: #222; margin-bottom: 8px;
  }
  .contact__list--phone li { font-weight: 800; }
  .contact__list--phone { margin-bottom: 18px; }
  .contact__list--web li { font-family: "Questrial", sans-serif; font-size: 14.5px; }
  .icon { width: 20px; height: 20px; flex: none; }
</style>
</head>
<body>

<section class="card card--front" aria-label="Vorderseite">
  <div class="brand">
    <span class="brand__name">velario</span>
    <span class="brand__tag">FINANCE CONSULTING</span>
  </div>
  <p class="legal">FREIER VERSICHERUNGSMAKLER MIT ERLAUBNIS NACH §34D ABS.1 GEWO<br>
  ERLAUBNISBEHÖRDE: HANDELSKAMMER SAALFURT, LINDENALLEE 12, 07391 SAALFURT – REG.-NR. D-3KPL-R82TQ-41</p>
</section>

<section class="card card--back" aria-label="Rückseite">
  <div class="brand">
    <span class="brand__name">velario</span>
    <span class="brand__tag">FINANCE CONSULTING</span>
  </div>
  <div class="contact">
    <h1 class="contact__name">LARS BRENNER</h1>
    <p class="contact__role">Geschäftsführer</p>
    <ul class="contact__list contact__list--phone">
      <li><svg class="icon" viewBox="0 0 20 20"><circle cx="10" cy="10" r="10" fill="#ef1c26"/><path d="M6 8.5c0-2 8-2 8 0v1h-2.2v-1h-3.6v1H6z M7 10.5h6l1 3H6z" fill="#fff"/></svg>T: 0170-555 12 34</li>
      <li><svg class="icon" viewBox="0 0 20 20"><circle cx="10" cy="10" r="10" fill="#ef1c26"/><rect x="7" y="4.5" width="6" height="11" rx="1" fill="#fff"/><rect x="8" y="6" width="4" height="7" fill="#ef1c26"/></svg>M: 0341-5550182</li>
      <li><svg class="icon" viewBox="0 0 20 20"><circle cx="10" cy="10" r="10" fill="#ef1c26"/><rect x="7.5" y="5" width="5" height="4" fill="#fff"/><rect x="5" y="9" width="10" height="6" rx="1" fill="#fff"/><rect x="7" y="11" width="6" height="1.2" fill="#ef1c26"/></svg>F: 0341-5550183</li>
    </ul>
    <ul class="contact__list contact__list--web">
      <li><svg class="icon" viewBox="0 0 20 20"><circle cx="10" cy="10" r="10" fill="#ef1c26"/><path d="M10 4.5a3.5 3.5 0 0 1 3.5 3.5c0 2.5-3.5 7-3.5 7s-3.5-4.5-3.5-7A3.5 3.5 0 0 1 10 4.5z" fill="#fff"/><circle cx="10" cy="8" r="1.3" fill="#ef1c26"/></svg>Birkenweg 47 04277 Leipzig</li>
      <li><svg class="icon" viewBox="0 0 20 20"><circle cx="10" cy="10" r="10" fill="#ef1c26"/><rect x="5" y="6.5" width="10" height="7" fill="#fff"/><path d="M5 6.5l5 4 5-4" fill="none" stroke="#ef1c26" stroke-width="1.2"/></svg>lars.brenner@velario.de</li>
      <li><svg class="icon" viewBox="0 0 20 20"><circle cx="10" cy="10" r="10" fill="#ef1c26"/><circle cx="10" cy="10" r="5" fill="none" stroke="#fff" stroke-width="1.3"/><ellipse cx="10" cy="10" rx="2" ry="5" fill="none" stroke="#fff" stroke-width="1.1"/><path d="M5 10h10" stroke="#fff" stroke-width="1.1"/></svg>www.velario.de</li>
    </ul>
  </div>
</section>

</body>
</html>
```